Web Design Project

Psychotherapy and Counselling Practice needs a landing page web design.

My business "Larkspur Advisory" specialises in the treatment of Anxiety and Depression with a holistic approach, endeavouring to unlock the key that holds us to ransom in a life that is imbalanced, frustrating, and ultimately of our own making due to our own perceptions and behaviours.

There is much that impacts us which we cannot change, but we are always in control of how we think, and how we frame our experiences.....learning to challenge those thoughts and behaviours that are destructive and disempowering opens up a world of joyful possibility. Life is about making choices, learn to make wiser and healthier choices.......

Larkspur Advisory has a client base of individual clients but will seek to expand to offer services to the Corporate world by offering an adjunct to employers for established "Wellness Programs".

Larkspur Advisory is a highly professional, ethically bound business, with the needs of the client at the forefront of all we do.

Larkspur Advisory wishes to avoid the usual "jargon driven" psychobabble offered on many counselling web pages. It aims to be stylishly presented, clean in look and with as few "words" as possible and a largely white background (faster loading and more powerful impact of what is stated), those words contained in the webpage should be meaningful, persuasive and have an impact simply at glance. Larkspur does not want , or expect, those prospective clients in need of support , to be reading through volumes of industry driven cliches.

At this point Larkspur is just looking for a high quality landing page. However in time this will likely expand to include other sections such as case studies, video content etc.

Target Market(s)

Those in need of emotional support, suffering mental health issues, and those simply wanting to become self aware supported by a mindful therapist.

Industry/Entity Type

Industry

Requirements
Must have
• The design must incorporate the Larkspur logo and colour schemes found on the attached files.

```html
<!DOCTYPE html>
<html lang="en">
<head>
<meta charset="utf-8">
<title>Larkspur Advisory</title>
<link rel="stylesheet" href="https://fonts.googleapis.com/css2?family=Arimo:ital,wght@0,400;0,700;1,400&display=swap">
<style>
  :root {
    --green: #7a9a01;
    --green-dark: #5f7d00;
    --green-light: #b3cb5c;
    --nav-top: #86a40a;
    --nav-bottom: #6a8a00;
    --text: #666666;
    --text-dark: #222222;
    --card: #f1f1f1;
    --band: #e2e2e2;
    --page-top: #efefef;
    --page-bottom: #cdcdcd;
    --bar-top: #7a7a7a;
    --bar-bottom: #454545;
    --white: #ffffff;
  }
  * { box-sizing: border-box; margin: 0; padding: 0; }
  html, body { width: 1200px; height: 939px; overflow: hidden; }
  body {
    position: relative;
    font-family: "Arimo", Arial, sans-serif;
    color: var(--text);
    background:
      radial-gradient(circle at 175px 80px, rgba(255,255,255,0.95) 0, rgba(255,255,255,0) 150px),
      linear-gradient(180deg, var(--page-top) 0%, var(--page-bottom) 100%);
  }
  .abs { position: absolute; }

  /* header */
  .brand-name {
    left: 90px; top: 92px;
    font-size: 29px; font-weight: 400; letter-spacing: 1px;
    color: var(--green);
  }
  .profile-photo {
    left: 753px; top: 19px; width: 92px; height: 98px;
    border: 3px solid var(--white); border-radius: 3px;
    box-shadow: 0 1px 4px rgba(0,0,0,0.3);
    background: linear-gradient(160deg, #c9c2bb 0%, #8d8077 55%, #3b4350 100%);
  }
  .profile-name { left: 862px; top: 16px; font-size: 23px; color: #6f6f6f; }
  .profile-title { left: 862px; top: 45px; font-size: 14.5px; color: #777; }
  .profile-contact { left: 862px; top: 74px; font-size: 14.5px; color: var(--green); line-height: 27px; }
  .profile-contact .email { font-size: 16.5px; }

  .main-nav {
    left: 534px; top: 152px; width: 577px; height: 100px;
    display: flex;
    background: linear-gradient(180deg, var(--nav-top) 0%, var(--nav-bottom) 100%);
    border-radius: 4px 4px 0 0;
  }
  .main-nav a {
    height: 100%; padding-top: 15px;
    color: var(--white); text-decoration: none; font-size: 14.5px; text-align: center;
    border-right: 1px solid rgba(0,0,0,0.12);
    box-shadow: inset -1px 0 0 rgba(255,255,255,0.08);
  }
  .main-nav a:last-child { border-right: none; box-shadow: none; }

  .stage { left: 0; top: 0; width: 1200px; height: 939px; pointer-events: none; }

  /* content */
  .section-title { font-size: 20.5px; font-weight: 700; color: var(--green); }
  .welcome-title { left: 105px; top: 290px; }
  .welcome-text {
    left: 106px; top: 324px; width: 681px;
    font-size: 13.6px; line-height: 23px; text-align: justify;
  }
  .divider { left: 102px; top: 457px; width: 687px; height: 1px; background: #dcdcdc; }
  .research-title { left: 104px; top: 471px; }

  .research-card {
    top: 511px; width: 208px; height: 239px;
    background: var(--card); border-radius: 3px;
    padding: 13px 17px;
  }
  .research-card h3 {
    font-size: 14.5px; font-weight: 400; line-height: 21px; color: var(--green-dark);
    margin-bottom: 9px;
  }
  .research-card p { font-size: 13.6px; line-height: 21px; text-align: justify; color: #777; }
  .view-more {
    position: absolute; left: 17px; bottom: 14px;
    font-size: 11px; font-weight: 700; color: var(--text-dark);
  }
  .view-more span { font-size: 14px; margin-left: 4px; }

  .newsletter {
    left: 106px; top: 765px; width: 681px; height: 67px;
    background: linear-gradient(180deg, var(--bar-top), var(--bar-bottom));
    border-radius: 3px;
  }
  .newsletter-icon { position: absolute; left: 29px; top: 17px; }
  .newsletter-label {
    position: absolute; left: 86px; top: 21px;
    font-size: 20.5px; font-weight: 700; color: var(--white);
  }
  .newsletter-field {
    position: absolute; left: 319px; top: 12px; width: 334px; height: 42px;
    background: var(--white); border-radius: 3px;
    box-shadow: inset 0 1px 3px rgba(0,0,0,0.25);
  }
  .newsletter-field .placeholder {
    position: absolute; left: 17px; top: 12px; font-size: 14px; color: #888;
  }
  .newsletter-button {
    position: absolute; right: 3px; top: 3px; width: 100px; height: 36px;
    background: linear-gradient(180deg, #555, #2f2f2f);
    border-radius: 3px;
    color: #eee; font-size: 15.5px; font-weight: 700; text-align: center; line-height: 36px;
  }

  .side-title { left: 813px; }
  .more-dot {
    width: 19px; height: 19px; border-radius: 50%; background: #c2c2c2;
  }
  .news-item {
    left: 811px; width: 287px; height: 121px;
    background: var(--card); border-radius: 3px;
  }
  .news-date { position: absolute; left: 20px; top: 22px; width: 34px; text-align: center; }
  .news-date .month { font-size: 12.5px; color: #333; margin-top: 2px; }
  .news-text {
    position: absolute; left: 68px; top: 14px; width: 202px;
    font-size: 13.6px; line-height: 23px; color: #777;
  }
  .testimonial {
    left: 811px; top: 654px; width: 287px; height: 178px;
    background: var(--card); border-radius: 3px;
    padding: 16px 17px;
  }
  .testimonial blockquote {
    font-style: italic; font-size: 13.6px; line-height: 23px; color: #777; text-align: justify;
  }
  .quote-mark { font-style: normal; font-weight: 700; font-size: 26px; color: #555; line-height: 0; vertical-align: -9px; }
  .testimonial cite { display: block; font-style: normal; font-size: 14px; color: #111; margin-top: 6px; }

  /* footer */
  .footer-nav { left: 90px; top: 865px; font-size: 14px; color: #333; word-spacing: 2px; }
  .footer-nav .sep { margin: 0 10px; }
  .copyright { left: 90px; top: 898px; font-size: 14px; color: #333; word-spacing: 2px; }
  .social { top: 888px; width: 24px; height: 24px; border-radius: 3px; }
  .social-one { left: 1055px; background: #3b5a9a; }
  .social-two { left: 1086px; background: #4fb4e6; }
</style>
</head>
<body>

  <div class="abs brand-name">LARKSPUR</div>

  <div class="abs profile-photo" role="img" aria-label="Portrait photograph of the therapist"></div>
  <div class="abs profile-name">Morgan Hale BA</div>
  <div class="abs profile-title">(Psych) BSc (Hons) Psych MBPS</div>
  <div class="abs profile-contact">
    <div>Mobile : 0412 338 906</div>
    <div>E-mail : <span class="email">morgan.hale@larkspurmail.com</span></div>
  </div>

  <nav class="abs main-nav">
    <a style="width:82px">Home</a>
    <a style="width:93px">About us</a>
    <a style="width:93px">Services</a>
    <a style="width:100px">Programs</a>
    <a style="width:100px">Seminars</a>
    <a style="width:109px">Contact us</a>
  </nav>

  <svg class="abs stage" viewBox="0 0 1200 939" aria-hidden="true">
    <path d="M700,247 C860,252 1010,228 1111,190 L1111,262 L700,262 Z" fill="var(--green-light)"/>
    <path d="M90,196 C220,172 380,182 560,217 C720,248 880,258 1111,232 L1111,244 C880,272 720,262 560,231 C380,196 220,188 90,210 Z" fill="var(--green)"/>
    <path d="M90,210 C220,188 380,196 560,231 C720,262 880,272 1111,244 L1111,260 C880,286 720,276 560,244 C380,210 220,204 90,224 Z" fill="var(--band)"/>
    <path d="M90,224 C220,204 380,210 560,244 C720,276 880,286 1111,260 L1111,838 Q1111,842 1107,842 L94,842 Q90,842 90,838 Z" fill="var(--white)"/>
  </svg>

  <h1 class="abs section-title welcome-title">Welcome to Larkspur</h1>
  <p class="abs welcome-text">Cras vestibulum a massa at pharetra. Nunc sed lacinia velit, eu commodo elit. Maecenas porta nec velit in pharetra. Cras tortor neque, pretium ut nibh a, facilisis iaculis arcu. Interdum et malesuada fames ac ante ipsum primis in faucibus. Curabitur gravida metus ut urna dapibus vulputate eget sed sem. Aenean tincidunt, tortor at tris tique condimentum, felis neque mollis massa, quis interdum eros leo ac est. Donec sit amet odio eget nibh convallis ultricies. Cum sociis natoque penatibus et magnis dis parturient montes,c</p>
  <div class="abs divider"></div>

  <h2 class="abs section-title research-title">Our Research</h2>

  <article class="abs research-card" style="left:106px">
    <h3>Nullam magna lectus, odio sollicitudin eu lorem id</h3>
    <p>Aliquam mi eleifend consect etur, libero velit congue nibh, et porttitor sapien. Morbi ac iaculis velit. Ut mollis imperdiet tortor at sceleris-que enim sit amet..</p>
    <div class="view-more">VIEW MORE<span>»</span></div>
  </article>
  <article class="abs research-card" style="left:343px">
    <h3>Nullam magna lectus, odio sollicitudin eu lorem id</h3>
    <p>Aliquam mi eleifend consect etur, libero velit congue nibh, et porttitor sapien. Morbi ac iaculis velit. Ut mollis imperdiet tortor at sceleris-que enim sit amet..</p>
    <div class="view-more">VIEW MORE<span>»</span></div>
  </article>
  <article class="abs research-card" style="left:579px">
    <h3>Nullam magna lectus, odio sollicitudin eu lorem id</h3>
    <p>Aliquam mi eleifend consect etur, libero velit congue nibh, et porttitor sapien. Morbi ac iaculis velit. Ut mollis imperdiet tortor at sceleris-que enim sit amet..</p>
    <div class="view-more">VIEW MORE<span>»</span></div>
  </article>

  <section class="abs newsletter">
    <svg class="newsletter-icon" width="44" height="30" viewBox="0 0 44 30" aria-hidden="true">
      <rect x="1" y="1" width="42" height="28" rx="1" fill="#f4f4f4" stroke="#bbb"/>
      <path d="M1,1 L22,17 L43,1" fill="none" stroke="#aaa" stroke-width="1.5"/>
      <path d="M1,29 L17,13 M43,29 L27,13" fill="none" stroke="#ccc" stroke-width="1"/>
    </svg>
    <div class="newsletter-label">Newsletter Subscribe</div>
    <div class="newsletter-field">
      <span class="placeholder">Enter your mail ID</span>
      <div class="newsletter-button">Subscribe</div>
    </div>
  </section>

  <h2 class="abs section-title side-title" style="top:290px">Latest News &amp; Events</h2>
  <div class="abs more-dot" style="left:1062px;top:289px"></div>
  <svg class="abs" style="left:1062px;top:289px" width="19" height="19" viewBox="0 0 19 19" aria-hidden="true"><path d="M8,5 L12,9.5 L8,14" fill="none" stroke="#fff" stroke-width="2"/></svg>

  <div class="abs news-item" style="top:330px">
    <div class="news-date">
      <svg width="30" height="28" viewBox="0 0 30 28" aria-hidden="true">
        <rect x="1.5" y="4" width="27" height="22.5" rx="2" fill="none" stroke="#666" stroke-width="2.5"/>
        <rect x="1.5" y="4" width="27" height="6" fill="#666"/>
        <rect x="7" y="0.5" width="3" height="6" fill="#666"/><rect x="20" y="0.5" width="3" height="6" fill="#666"/>
        <text x="15" y="23" font-family="Arimo, Arial, sans-serif" font-size="10.5" font-weight="700" fill="#555" text-anchor="middle">17</text>
      </svg>
      <div class="month">June</div>
    </div>
    <p class="news-text">Tnascetur ridiculus mus. Aenean pharetra neque vel est hendrerit dapibus. Morbi dapibus metus ac nisi ultricies.</p>
  </div>
  <div class="abs news-item" style="top:459px">
    <div class="news-date">
      <svg width="30" height="28" viewBox="0 0 30 28" aria-hidden="true">
        <rect x="1.5" y="4" width="27" height="22.5" rx="2" fill="none" stroke="#666" stroke-width="2.5"/>
        <rect x="1.5" y="4" width="27" height="6" fill="#666"/>
        <rect x="7" y="0.5" width="3" height="6" fill="#666"/><rect x="20" y="0.5" width="3" height="6" fill="#666"/>
        <text x="15" y="23" font-family="Arimo, Arial, sans-serif" font-size="10.5" font-weight="700" fill="#555" text-anchor="middle">17</text>
      </svg>
    </div>
    <p class="news-text">Tnascetur ridiculus mus. Aenean pharetra neque vel est hendrerit dapibus. Morbi dapibus metus ac nisi ultricies.</p>
  </div>

  <h2 class="abs section-title side-title" style="top:615px">Client’s Testimonials</h2>
  <div class="abs more-dot" style="left:1062px;top:613px"></div>
  <svg class="abs" style="left:1062px;top:613px" width="19" height="19" viewBox="0 0 19 19" aria-hidden="true"><path d="M8,5 L12,9.5 L8,14" fill="none" stroke="#fff" stroke-width="2"/></svg>

  <div class="abs testimonial">
    <blockquote><span class="quote-mark">“</span> Phasellus et magna id ante egestas henlibero, a sagittis lorem porta vitae. Quisque dapibus turpis fringilla, eget commodo felis interdum. Sed blandit felis ipsum, sed quam orci, et cursus <span class="quote-mark">”</span></blockquote>
    <cite>Client name, City</cite>
  </div>

  <div class="abs footer-nav">Home<span class="sep">|</span>About us<span class="sep">|</span>Services<span class="sep">|</span>Programs<span class="sep">|</span>Seminars<span class="sep">|</span>Contact us</div>
  <div class="abs copyright">Copyright&nbsp; ©&nbsp; 2013&nbsp;&nbsp;&nbsp; www.larkspuradvisory.com.au&nbsp;&nbsp;&nbsp; All rights reserved.</div>
  <div class="abs social social-one"></div>
  <div class="abs social social-two"></div>

</body>
</html>
```